Construction company stationary design

We're wanting to develop a new professional stationary set for a newly establised property related business using our existing logo (attached). Business incorporates renovations, property investment and property development.

Specifically needing letter head, business cards, envelopes, email signature and need to get tshirt and caps embroydered.

Looking for something quite modern but professional using white, black and green.

```html
<!DOCTYPE html>
<html lang="en">
<head>
<meta charset="utf-8">
<title>Ridgemont Constructions – Business Cards</title>
<link rel="stylesheet" href="https://fonts.googleapis.com/css2?family=Source+Sans+3:wght@400;600;700;800&display=swap">
<style>
  :root {
    --green: #84c241;
    --white: #ffffff;
    --black: #000000;
    --ink: #333333;
    --ink-light: #f2f2f2;
    --backdrop: #e9e6e1;
  }
  * { margin: 0; padding: 0; box-sizing: border-box; }
  html, body { width: 1200px; height: 720px; overflow: hidden; }
  body {
    background: var(--backdrop);
    font-family: "Source Sans 3", "Myriad Pro", Arial, sans-serif;
    position: relative;
  }
  .card {
    position: absolute;
    width: 555px;
    height: 316px;
    overflow: hidden;
  }
  .card--front-light { left: 25px; top: 23px; background: var(--white); color: var(--ink); }
  .card--back-green  { left: 613px; top: 23px; background: var(--green); color: var(--white); }
  .card--front-dark  { left: 25px; top: 372px; background: var(--black); color: var(--ink-light); }
  .card--back-dark   { left: 613px; top: 372px; background: var(--black); color: var(--green); }

  /* Wordmark */
  .wordmark { display: flex; align-items: center; gap: 10px; font-weight: 800; line-height: 0.95; }
  .wordmark__square { width: 22px; height: 22px; background: currentColor; flex: none; }
  .wordmark__name { display: flex; flex-direction: column; }
  .wordmark__main { font-size: 50px; letter-spacing: 1px; }
  .wordmark__sub  { font-size: 19.5px; letter-spacing: 2.6px; }

  /* Front cards */
  .front__logo { position: absolute; left: 22px; top: 62px; color: var(--green); }
  .front__person {
    position: absolute; left: 23px; top: 197px;
    font-size: 18px; font-weight: 700; color: var(--green); letter-spacing: 0.2px;
  }
  .contact { position: absolute; left: 23px; top: 233px; font-size: 15px; line-height: 22px; }
  .contact__row { display: flex; align-items: center; gap: 6px; }
  .contact__item { display: inline-flex; align-items: center; gap: 5px; margin-right: 6px; }
  .contact__icon { width: 12px; height: 12px; color: var(--green); flex: none; }
  .front__address { position: absolute; left: 23px; top: 282px; font-size: 15px; }

  /* Back cards */
  .back__logo { position: absolute; left: 0; right: 0; top: 92px; display: flex; justify-content: center; }
  .back__logo .wordmark__main { font-size: 62px; }
  .back__logo .wordmark__sub { font-size: 24px; letter-spacing: 3.3px; }
  .back__url {
    position: absolute; left: 0; right: 0; top: 276px; text-align: center;
    font-size: 17px; font-weight: 600; letter-spacing: 4px; color: var(--white);
  }
</style>
</head>
<body>

<svg width="0" height="0" style="position:absolute">
  <defs>
    <symbol id="icon-phone" viewBox="0 0 12 12"><circle cx="6" cy="6" r="5.3" fill="none" stroke="currentColor" stroke-width="1.2"/><path d="M4 3.2 5.2 4.6 4.6 5.4c.5 1 1.1 1.6 2 2l.8-.6 1.4 1.2-.8 1C6 8.8 3.5 6.3 3.2 4z" fill="currentColor"/></symbol>
    <symbol id="icon-mobile" viewBox="0 0 12 12"><rect x="3" y="0.8" width="6" height="10.4" rx="1" fill="currentColor"/><rect x="4" y="2" width="4" height="6" fill="#fff" opacity=".6"/></symbol>
    <symbol id="icon-mail" viewBox="0 0 12 12"><path d="M1 5 6 1.8 11 5v5.5H1z" fill="currentColor"/><path d="M1.5 5.2 6 8l4.5-2.8" fill="none" stroke="#fff" stroke-width=".9"/></symbol>
    <symbol id="icon-globe" viewBox="0 0 12 12"><circle cx="6" cy="6" r="5.3" fill="currentColor"/><path d="M.8 6h10.4M6 .8v10.4M2 3.3h8M2 8.7h8" stroke="#fff" stroke-width=".7" fill="none"/><ellipse cx="6" cy="6" rx="2.4" ry="5.3" fill="none" stroke="#fff" stroke-width=".7"/></symbol>
  </defs>
</svg>

<!-- Front, light -->
<section class="card card--front-light">
  <div class="front__logo wordmark">
    <span class="wordmark__square"></span>
    <span class="wordmark__name"><span class="wordmark__main">RIDGEMONT</span><span class="wordmark__sub">CONSTRUCTIONS</span></span>
  </div>
  <p class="front__person">PERSONS NAME</p>
  <div class="contact">
    <div class="contact__row">
      <span class="contact__item"><svg class="contact__icon"><use href="#icon-phone"/></svg>0123 456789</span>
      <span class="contact__item"><svg class="contact__icon"><use href="#icon-mobile"/></svg>0123 456789</span>
    </div>
    <div class="contact__row">
      <span class="contact__item"><svg class="contact__icon"><use href="#icon-mail"/></svg>info@ridgemont.com</span>
      <span class="contact__item"><svg class="contact__icon"><use href="#icon-globe"/></svg>www.ridgemont.com</span>
    </div>
  </div>
  <p class="front__address">00, Complex name, City, State 0042</p>
</section>

<!-- Back, green -->
<section class="card card--back-green">
  <div class="back__logo">
    <div class="wordmark">
      <span class="wordmark__square"></span>
      <span class="wordmark__name"><span class="wordmark__main">RIDGEMONT</span><span class="wordmark__sub">CONSTRUCTIONS</span></span>
    </div>
  </div>
  <p class="back__url">www.ridgemont.com</p>
</section>

<!-- Front, dark -->
<section class="card card--front-dark">
  <div class="front__logo wordmark">
    <span class="wordmark__square"></span>
    <span class="wordmark__name"><span class="wordmark__main">RIDGEMONT</span><span class="wordmark__sub">CONSTRUCTIONS</span></span>
  </div>
  <p class="front__person">PERSONS NAME</p>
  <div class="contact">
    <div class="contact__row">
      <span class="contact__item"><svg class="contact__icon"><use href="#icon-phone"/></svg>0123 456789</span>
      <span class="contact__item"><svg class="contact__icon"><use href="#icon-mobile"/></svg>0123 456789</span>
    </div>
    <div class="contact__row">
      <span class="contact__item"><svg class="contact__icon"><use href="#icon-mail"/></svg>info@ridgemont.com</span>
      <span class="contact__item"><svg class="contact__icon"><use href="#icon-globe"/></svg>www.ridgemont.com</span>
    </div>
  </div>
  <p class="front__address">00, Complex name, City, State 0042</p>
</section>

<!-- Back, dark -->
<section class="card card--back-dark">
  <div class="back__logo">
    <div class="wordmark">
      <span class="wordmark__square"></span>
      <span class="wordmark__name"><span class="wordmark__main">RIDGEMONT</span><span class="wordmark__sub">CONSTRUCTIONS</span></span>
    </div>
  </div>
  <p class="back__url">www.ridgemont.com</p>
</section>

</body>
</html>
```